Food Safety 1-California workers only

3.25" by 4.5" Black and White Magazine Ad
This ad is to train California workers only.
Workers will be trained on: Food Safety, FSMA (Food Safety Modernization Act), using equipment safety, food processing production skills, worker safety, supervisory skills, communication skills.
"FREE TRAINING", The company does the training or Keystone Learning will provide the training.
Training grants range from $100,000 to $400,000.
Companies must be in business for profit.
Companies must train 200 employees or more.
This program is for California workers only.
Incumbent or new-hires are eligible.

Target Market(s)

California food processors, farms, food packaging, food processors, companies under FSMA, food safety, food production who need to train employees.

Industry/Entity Type

Food Production

Font styles to use
Serif
Sans Serif

Colors

Designer to choose colors to be used in the design.

Requirements
Must have
• This is a 3.25 inch by 4.5 inch magazine ad. It must be black and white. No color.
• The deliverable must be in basic PhotoShop. The ad does not need to include any graphics and be text only if needed. If you have a black and white graphic that will show well.
• Look at www.KLGFoodSafety..com
• Use the text from "MEALBOX-Photoshop-052018" file as your starting point.
Nice to have
• A black and white graphic about food. See www.KLGFoodSafety.com
Should not have
• No color.

```html
<!DOCTYPE html>
<html lang="en">
<head>
<meta charset="utf-8">
<title>Free Training – Keystone Learning</title>
<link rel="stylesheet" href="https://fonts.googleapis.com/css2?family=Oswald:wght@700&family=Raleway:wght@300;400;700;800&family=PT+Sans+Narrow&family=Open+Sans:wght@400&display=swap">
<style>
  :root {
    --page-bg: #d9d9d9;
    --header-bg: #232323;
    --body-bg: #2e2e2e;
    --footer-bg: #1f1f1f;
    --callout-bg: #4a4a4a;
    --panel-light: #e9e9e9;
    --contact-bg: #1c1c1c;
    --ink-light: #f4f4f4;
    --ink-muted: #d6d6d6;
    --ink-dark: #2a2a2a;
  }
  html, body { margin: 0; padding: 0; width: 1200px; height: 1200px; overflow: hidden; background: var(--page-bg); }
  .ad { position: absolute; left: 192px; top: 36px; width: 816px; height: 1128px; background: var(--body-bg); overflow: hidden; }
  .header { position: absolute; left: 0; top: 0; width: 816px; height: 254px; background: var(--header-bg); text-align: center; color: var(--ink-light); }
  .header__title { position: absolute; left: 0; right: 0; top: 36px; margin: 0; font-family: "Oswald", sans-serif; font-weight: 700; font-size: 94px; line-height: 1; letter-spacing: 1px; }
  .header__topics { position: absolute; left: 0; right: 0; font-family: "Raleway", sans-serif; font-size: 27px; margin: 0; white-space: nowrap; }
  .header__topics--one { top: 146px; }
  .header__topics--two { top: 185px; }
  .header__topics span { margin: 0 8px; }
  .header__topics span::before { content: "\2022"; margin-right: 6px; }
  .photo { position: absolute; left: 0; top: 254px; width: 816px; height: 492px; background: linear-gradient(100deg, #9a9a9a 0%, #c8c8c8 40%, #e4e4e4 70%, #bdbdbd 100%); }
  .callout { position: absolute; left: 60px; top: 794px; width: 336px; height: 214px; background: var(--callout-bg); color: var(--ink-light); font-family: "Raleway", sans-serif; }
  .callout p { margin: 0; position: absolute; left: 50px; white-space: nowrap; line-height: 1; }
  .callout__l1 { top: 24px; font-size: 39px; font-weight: 300; }
  .callout__l2 { top: 72px; font-size: 31px; font-weight: 400; }
  .callout__l2 b { font-weight: 800; }
  .callout__l3 { top: 112px; font-size: 41px; font-weight: 800; }
  .callout__l4 { top: 160px; font-size: 41px; font-weight: 800; }
  .footer { position: absolute; left: 0; top: 1054px; width: 816px; height: 74px; background: var(--footer-bg); }
  .footer__web { position: absolute; left: 48px; top: 22px; display: flex; align-items: center; gap: 8px; color: var(--ink-muted); font-family: "Open Sans", sans-serif; font-size: 17px; }
  .eligibility { position: absolute; left: 453px; top: 588px; width: 347px; height: 540px; background: var(--panel-light); }
  .eligibility ul { list-style: none; margin: 0; padding: 0; position: absolute; left: 32px; top: 24px; }
  .eligibility li { display: flex; align-items: center; gap: 12px; height: 31.4px; font-family: "PT Sans Narrow", sans-serif; font-size: 18.5px; color: var(--ink-dark); white-space: nowrap; }
  .contact { position: absolute; left: 472px; top: 904px; width: 344px; height: 224px; background: var(--contact-bg); color: var(--ink-muted); font-family: "Open Sans", sans-serif; font-size: 18px; }
  .contact__row { position: absolute; left: 30px; display: flex; gap: 12px; align-items: flex-start; line-height: 23px; }
  .contact__row svg { flex: none; margin-top: 2px; }
  .contact__name { top: 16px; }
  .contact__address { top: 54px; font-size: 17px; }
  .contact__email { top: 134px; }
  .contact__phone { top: 169px; }
</style>
</head>
<body>
<div class="ad">
  <header class="header">
    <h1 class="header__title">FREE TRAINING</h1>
    <p class="header__topics header__topics--one"><span>Food Safety</span><span>FSMA</span><span>Production Skills</span></p>
    <p class="header__topics header__topics--two"><span>Supervisory skills</span><span>Worker Safety</span></p>
  </header>

  <div class="photo" role="img" aria-label="Black and white photo of a trainer presenting at a flip chart to seated workshop attendees"></div>

  <div class="callout">
    <p class="callout__l1">WE DO THE</p>
    <p class="callout__l2"><b>TRAINING</b> AND</p>
    <p class="callout__l3">THE STATE</p>
    <p class="callout__l4">PAYS FOR IT</p>
  </div>

  <footer class="footer">
    <div class="footer__web">
      <svg width="26" height="26" viewBox="0 0 26 26" fill="none" stroke="#d6d6d6" stroke-width="1.6"><circle cx="13" cy="13" r="10"/><ellipse cx="13" cy="13" rx="4.5" ry="10"/><line x1="3" y1="13" x2="23" y2="13"/></svg>
      <span>www.KLGCAL.com | www.KLGFoodSafety.com</span>
    </div>
  </footer>

  <section class="eligibility">
    <ul>
      <li><svg width="18" height="18" viewBox="0 0 18 18" fill="none" stroke="#2a2a2a" stroke-width="2"><path d="M14 9v6H3V4h8"/><path d="M6 8l3 3 7-8"/></svg>Train California Workers Only</li>
      <li><svg width="18" height="18" viewBox="0 0 18 18" fill="none" stroke="#2a2a2a" stroke-width="2"><path d="M14 9v6H3V4h8"/><path d="M6 8l3 3 7-8"/></svg>Trainees must earn $11/hour</li>
      <li><svg width="18" height="18" viewBox="0 0 18 18" fill="none" stroke="#2a2a2a" stroke-width="2"><path d="M14 9v6H3V4h8"/><path d="M6 8l3 3 7-8"/></svg>Full-time workers only</li>
      <li><svg width="18" height="18" viewBox="0 0 18 18" fill="none" stroke="#2a2a2a" stroke-width="2"><path d="M14 9v6H3V4h8"/><path d="M6 8l3 3 7-8"/></svg>Employees must attend at least 8</li>
      <li><svg width="18" height="18" viewBox="0 0 18 18" fill="none" stroke="#2a2a2a" stroke-width="2"><path d="M14 9v6H3V4h8"/><path d="M6 8l3 3 7-8"/></svg>Hours of training</li>
      <li><svg width="18" height="18" viewBox="0 0 18 18" fill="none" stroke="#2a2a2a" stroke-width="2"><path d="M14 9v6H3V4h8"/><path d="M6 8l3 3 7-8"/></svg>You must train 200 or more employees</li>
      <li><svg width="18" height="18" viewBox="0 0 18 18" fill="none" stroke="#2a2a2a" stroke-width="2"><path d="M14 9v6H3V4h8"/><path d="M6 8l3 3 7-8"/></svg>Incumbent or New-Hire workers are eligible</li>
      <li><svg width="18" height="18" viewBox="0 0 18 18" fill="none" stroke="#2a2a2a" stroke-width="2"><path d="M14 9v6H3V4h8"/><path d="M6 8l3 3 7-8"/></svg>Seasonal workers are eligible</li>
    </ul>
  </section>

  <section class="contact">
    <div class="contact__row contact__name">
      <svg width="20" height="22" viewBox="0 0 20 22" fill="#d6d6d6"><circle cx="10" cy="6" r="5"/><path d="M1 22c0-6 4-9 9-9s9 3 9 9z"/></svg>
      <span>Daniel Marsh</span>
    </div>
    <div class="contact__row contact__address">
      <svg width="20" height="26" viewBox="0 0 20 26" fill="none" stroke="#d6d6d6" stroke-width="1.6"><path d="M10 20C4 13 3 10 3 8a7 7 0 0 1 14 0c0 2-1 5-7 12z"/><circle cx="10" cy="8" r="2.5"/><ellipse cx="10" cy="23" rx="6" ry="2"/></svg>
      <span>Keystone Learning Company<br>Inc. 1800 Harbor View Drive Suite<br>310 Irvine, CA 92614</span>
    </div>
    <div class="contact__row contact__email">
      <svg width="24" height="20" viewBox="0 0 24 20" fill="none" stroke="#d6d6d6" stroke-width="1.6"><path d="M2 8l10-6 10 6v10H2z"/><path d="M2 8l10 6 10-6"/></svg>
      <span>Dan.Marsh@KLGCAL.com</span>
    </div>
    <div class="contact__row contact__phone">
      <svg width="22" height="22" viewBox="0 0 22 22" fill="none" stroke="#d6d6d6" stroke-width="1.8"><path d="M5 3l3 4-2 2c1 3 3 5 6 6l2-2 4 3-2 3C9 19 3 13 2 5z"/></svg>
      <span>(949) 555-0147</span>
    </div>
  </section>
</div>
</body>
</html>
```